4 Information One pagers needed for Australia's biggest Oil & Gas Conference

TVR is a global organisation with its corporate headquarters located in Perth, Western Australia and regional offices in Brisbane, Darwin, Singapore, Korea & China.
TVR delivers dedicated project support services, incorporating but not limited to; project design, procurement, construction, installation, commissioning, operations and maintenance. Our cross industry expertise, project expertise and track record of successfully delivering international projects with blue chip clients and partners has led to our fast evolving reputation as a preferred supplier worldwide within the oil and gas industry onshore and offshore within both greenfield and brownfield scopes.

Need to get information on a one page handout. There are 4 documents that need to be developed.

We need a banner across the top and bottom of each page, which has our logo, title of the document, and our contact details (Head Office – Address: Unit 14, 37-39 Harrow Lane, Perth WA 6000 Australia. Phone: +61 8 9471 5086) Needs to keep with the TVR colours but use images that are relevant to the oil and gas/commissioning industries. Our previous “who we are” flyer is attached so you have a feel for what we are after.

Page 1: TVR’ service offerings include (for each take brief paragraph from document attached for description of each. If unable to find information please contact us or search on www.fennmarsh-example.com):
• Engineering Design;
• Construction Management;
• Commissioning (Systems, Processes, Resources);
• Completions Strategy;
• Multi-Disciplinary Engineering;
• Multi-Disciplinary Technicians;
• Operations & Maintenance Support;
• EX Inspect & Maintain;
• On Site Nitrogen Production;
• Water Treatment;
• Compact Separation Systems;
• Processes to support services;
o Technology to improve efficiency and productivity (Finishline Bridge, QT Bridge).

Page 2: Our Team – please complete in order listed below and images are attached
Darren Kovalenko
Chief Executive Officer (CEO)
An extensively experienced and practical executive in the engineering industry with over 20 years’ service, more specifically in the oil and gas sector, since 1988.
The experience has been gained through a wide array of projects throughout Australia and Overseas working in the area of Design, System Analysing, Commissioning and Construction before commencing in Business Development and then finally Company Management and Directorships.
Darren has gained extensive experience in line and project management roles and more particularly in change management, people development and team motivation.
He has extensive experience leading and working in teams associated with design, construction and commissioning of world scale capital projects in both ‘brownfields’ and ‘Greenfields’ scenarios.
Keith Lambert
Chief Financial Officer
Keith is a qualified accountant (CGMA, CMA, CPA. MAAT) and brings to the team over 20 years of Australian and International experience in a number of key financial roles at both ASX listed and private companies. Keith comes to the team with a strong financial, commercial and business analytical skills combined with proven effective leadership of finance teams. Keith has significant experience in managing working capital requirements of growth businesses with an international footprint. Keith is a member of Australian Guild of Registered Ledger Advisers, Royal College of Cost Ledger Officers & Federation of Bookkeeping Practitioners.

Maree Tolvanen
HR Manager
Maree has more than 10 years’ experience across Oil & Gas, Resources, Engineering, and Finance industries. With general human resources experience, Maree has led strategic and operational HR support and services across recruitment, on boarding, training, remuneration and benefits, employment contract management, career planning and organisational accreditation for 457 visas. Further to this Maree has also managed HR within the M & A environment, through due diligence and post-acquisition integration on both buy and sell sides within the context of global organisations.

Gregory Nash
Project Services & Agency Representative
Project Services and Management expertise with local and international experience in the oil & gas, mining, and utilities industries, as well as a strong understanding within the finance sector. Gregory’s strengths and experience lie in developing and executing business proposals, as well as liaising with external consultants and clients. Possessing competent financial and economic modelling skills and the ability to utilise data for risk and profit based outcomes. Gregory has managed ISO 9001 implementation and ensures that all quality assurance processes are adhered to.
Gregory holds both Bachelor of Commerce and Master of Commerce (Economics & Finance) degrees and is working towards a Master of Science (Energy).

Trevor Dunstall
Director: TVR NT
Gregory has lived in the North of Australia for the last 26 years, bringing valuable local knowledge to the TVR NT office. He has owned and operated his NT services business for 17 years; servicing local and international clients before concentrating and moving into the Oil & Gas and Mining Sector. Gregory has many years of experience in logistics, service and supply, his extensive experience in the NT comes from the following industries: Oil & Gas; Mining; Exploration; Pastoral, Commercial Marine; and Construction.

Stuart Fenwick
Business Development Manager- Queensland
Stuart is a professional civil and mechanical engineer with more than 40 years’ experience in Australia and internationally, across consulting, construction and manufacturing sectors at operational and executive levels. He has held a number of senior executive roles with companies including Harlan Valve Systems, RTV Korvel, and Queensland Transit and has served on a number of industry associations, government committees and private sector boards.

Stuart has broad knowledge and experience in Australian and international business, with an extensive professional network throughout Australia, Asia, Europe and the United States. He has manufactured and supplied products to the oil and gas, petrochemical, power, water, military and nuclear industries.

Page 3: Our Influence
We need the headlines and logos of the following articles and publications:
https://www.tradewirewest.com.au/article/TVR-buys-Singapore-recruitment-firm?ref_K4pLmQ
http://www.fuelwirejournal-example.net/story.asp?id=413207591&section=careers
http://www.fuelwirejournal-example.net/story.asp?id=413207592&section=moves
Southern Crude & Pipeline Review – this one is getting published soon so just the logo for this one at this time?

Page 4: Who we work with?
Need to have just all logos of the companies that we have worked with. Attached is logos of our clients to match the list below. May need to find better resolution ones.
- Valtrop
- Kestrune Energy
- Norvane Global
- Brackmere
- MRP – Marlow Rigging Partners
- Tessaro
- Vantor Quell
- Hanul Coastal Fuel Company
- Corvo
- TL Group
- QN
- Lunden Rotors
- Orrin Petroleum
- Takka Energy
- Halberd Ridge Minerals (HRM)
- Wellspan Energy
- Tolsey Resources
- Glenrock Meats
- Drovan
- Pembury Ledger
- Varsell South Korea
- Clem Gully Iron Ore
- Westbrook Utility Holdings
- Falcrest Oil
- Solvant
- Tibbet Nickel
- Kvorn Oil
- Dravitel
- KMT
- Yarrandale Alumina

Industry/Entity Type

Oil And Gas

Font styles to use
Sans Serif
Other font styles liked:
• DIN Offc

Requirements
Must have
• 4 separate pages:
• 1. Menu of Services
• 2. Our Team
• 3. Our Influences (media companies)
• 4. Who we work with
• Keep in colours of TVR and ensure same header/footer used for all 4 pages
• orange = #D76927, R-215 G-105 B-39, CMYK C-11.65 M-70.4 Y-100 K-1.52
• Blue = #21224B, R-33 G-34 B-75, CMYK C-95.65, M-92.65 Y-39.82, K40.01
• Same theme across all 4
Nice to have
• Visually appealing
• Brief information
• Colour
• Images
Should not have
• Made up information - if unsure please contact us

```html
<!DOCTYPE html>
<html lang="en">
<head>
<meta charset="utf-8">
<title>TVR – Our Team</title>
<link href="https://fonts.googleapis.com/css2?family=Questrial&display=swap" rel="stylesheet">
<style>
:root{
  --navy:#21224b;
  --orange:#d76927;
  --grey:#9a9a9c;
  --ink:#1d1d24;
  --paper:#ffffff;
  --cream:#fff3e6;
}
*{margin:0;padding:0;box-sizing:border-box}
html,body{width:851px;height:1200px;overflow:hidden;background:var(--paper)}
body{font-family:"Questrial",sans-serif;color:var(--ink);position:relative}
.page{position:relative;width:851px;height:1200px;overflow:hidden}

.brand{position:absolute;left:66px;top:26px;display:flex;align-items:center;gap:10px}
.brand-mark{width:16px;height:16px;background:var(--orange)}
.brand-name{font-size:54px;letter-spacing:4px;color:var(--navy);line-height:1}
.page-title{position:absolute;left:344px;top:23px;width:485px;height:71px;background:var(--navy);
  color:#fff;font-size:36px;display:flex;align-items:center;justify-content:center;letter-spacing:.5px}
.rule{position:absolute;left:33px;top:117px;width:783px;height:1px;background:#c9b9aa}

.band{position:absolute;left:0;width:851px}
.band-navy-1{top:300px;height:187px;background:var(--navy);clip-path:polygon(0 26px,100% 0,100% 100%,0 165px)}
.band-orange{top:614px;height:192px;background:var(--orange);clip-path:polygon(0 32px,100% 0,100% 100%,0 171px)}
.band-navy-2{top:918px;height:191px;background:var(--navy);clip-path:polygon(0 35px,100% 0,100% 100%,0 100%)}

.photo{position:absolute;background:linear-gradient(160deg,#e9f3fb 0%,#8fc0e3 45%,#2d6ea6 100%)}
.photo.studio{background:linear-gradient(160deg,#f4f6f8 0%,#dfe5ea 100%)}

.member{position:absolute}
.member .name{font-size:15.5px;line-height:1.55}
.member .role{font-size:15.5px;line-height:1.55}
.member .bio{font-size:11.3px;line-height:18.4px;text-align:justify}
.member.right{text-align:right}
.member.right .bio{text-align-last:right}
.on-navy{color:#fff}
.on-orange{color:#fff}

.footer{position:absolute;left:0;top:1109px;width:851px;height:91px;
  background:linear-gradient(180deg,#e1702d 0%,#ef9a57 45%,#f2b57c 75%,#c86a2c 100%)}
.footer-info{position:absolute;left:23px;top:14px;color:var(--cream);font-size:13.5px;line-height:21px}
.footer-web{position:absolute;right:25px;top:20px;color:var(--cream);font-size:15.5px}
</style>
</head>
<body>
<div class="page">
  <header>
    <div class="brand"><span class="brand-name">TVR</span><span class="brand-mark"></span></div>
    <h1 class="page-title">OUR TEAM</h1>
    <div class="rule"></div>
  </header>

  <div class="band band-navy-1"></div>
  <div class="band band-orange"></div>
  <div class="band band-navy-2"></div>

  <div class="photo" style="left:17px;top:127px;width:210px;height:188px" role="img" aria-label="Portrait of Darren Kovalenko"></div>
  <section class="member" style="left:237px;top:126px;width:592px">
    <div class="name">Darren Kovalenko</div>
    <div class="role">Chief Executive Officer (CEO)</div>
    <p class="bio">An extensively experienced and practical executive in the engineering industry with over 20 years’ service, more specifically in the oil and gas sector, since 1988. The experience has been gained through a wide array of projects throughout Australia and Overseas working in the area of Design, System Analysing, Commissioning and Construction before commencing in Business Development and then finally Company Management and Directorships. Darren has gained extensive experience in line and project management roles and more particularly in change management, people development and team motivation. He has extensive experience leading and working in teams associated with design, construction and commissioning of world scale capital projects in both ‘brownfields’ and ‘Greenfields’ scenarios.</p>
  </section>

  <div class="photo" style="left:646px;top:310px;width:184px;height:165px" role="img" aria-label="Portrait of Keith Lambert"></div>
  <section class="member right on-navy" style="left:33px;top:311px;width:605px">
    <div class="name">Keith Lambert</div>
    <div class="role">Chief Financial Officer</div>
    <p class="bio">Keith is a qualified accountant (CGMA, CMA, CPA. MAAT) and brings to the team over 20 years of Australian and International experience in a number of key financial roles at both ASX listed and private companies. Keith comes to the team with a strong financial, commercial and business analytical skills combined with proven effective leadership of finance teams. Keith has significant experience in managing working capital requirements of growth businesses with an international footprint. Keith is a member of Australian Guild of Registered Ledger Advisers, Royal College of Cost Ledger Officers &amp; Federation of Bookkeeping Practitioners.</p>
  </section>

  <div class="photo" style="left:17px;top:470px;width:184px;height:164px" role="img" aria-label="Portrait of Maree Tolvanen"></div>
  <section class="member" style="left:209px;top:480px;width:620px">
    <div class="name">Maree Tolvanen</div>
    <div class="role">HR Manager</div>
    <p class="bio">Maree has more than 10 years’ experience across Oil &amp; Gas, Resources, Engineering, and Finance industries. With general human resources experience, Maree has led strategic and operational HR support and services across recruitment, on boarding, training, remuneration and benefits, employment contract management, career planning and organisational accreditation for 457 visas. Further to this Maree has also managed HR within the M &amp; A environment, through due diligence and post-acquisition integration on both buy and sell sides within the context of global organisations.</p>
  </section>

  <div class="photo" style="left:646px;top:629px;width:185px;height:163px" role="img" aria-label="Portrait of Gregory Nash"></div>
  <section class="member right on-orange" style="left:25px;top:626px;width:613px">
    <div class="name">Gregory Nash</div>
    <div class="role">Project Services &amp; Agency Representative</div>
    <p class="bio" style="line-height:16.6px">Project Services and Management expertise with local and international experience in the oil &amp; gas, mining, and utilities industries, as well as a strong understanding within the finance sector. Gregory’s strengths and experience lie in developing and executing business proposals, as well as liaising with external consultants and clients. Possessing competent financial and economic modelling skills and the ability to utilise data for risk and profit based outcomes. Gregory has managed ISO 9001 implementation and ensures that all quality assurance processes are adhered to. Gregory holds both Bachelor of Commerce and Master of Commerce (Economics &amp; Finance) degrees and is working towards a Master of Science (Energy).</p>
  </section>

  <div class="photo studio" style="left:16px;top:787px;width:184px;height:164px" role="img" aria-label="Portrait of Trevor Dunstall"></div>
  <section class="member" style="left:209px;top:795px;width:630px">
    <div class="name">Trevor Dunstall</div>
    <div class="role">Director: TVR NT</div>
    <p class="bio" style="line-height:17.5px">Gregory has lived in the North of Australia for the last 26 years, bringing valuable local knowledge to the TVR NT office. He has owned and operated his NT services business for 17 years; servicing local and international clients before concentrating and moving into the Oil &amp; Gas and Mining Sector. Gregory has many years of experience in logistics, service and supply, his extensive experience in the NT comes from the following industries: Oil &amp; Gas; Mining; Exploration; Pastoral, Commercial Marine; and Construction.</p>
  </section>

  <div class="photo studio" style="left:649px;top:935px;width:182px;height:162px" role="img" aria-label="Portrait of Stuart Fenwick"></div>
  <section class="member right on-navy" style="left:9px;top:933px;width:629px">
    <div class="name">Stuart Fenwick</div>
    <div class="role">Business Development Manager- Queensland</div>
    <p class="bio">Stuart is a professional civil and mechanical engineer with more than 40 years’ experience in Australia and internationally, across consulting, construction and manufacturing sectors at operational and executive levels. He has held a number of senior executive roles with companies including Harlan Valve Systems, RTV Korvel, and Queensland Transit and has served on a number of industry associations, government committees and private sector boards.</p>
    <p class="bio">Stuart has broad knowledge and experience in Australian and international business, with an extensive professional network throughout Australia, Asia, Europe and the United States. He has manufactured and supplied products to the oil and gas, petrochemical, power, water, military and nuclear industries.</p>
  </section>

  <footer class="footer" role="img" aria-label="Sunset scene with an offshore oil rig silhouette">
    <div class="footer-info">
      <div>Head Office</div>
      <div>Address: Unit 14, 37-39 Harrow Lane, Perth WA 6000 Australia</div>
      <div>Phone: +61 8 9471 5086</div>
    </div>
    <div class="footer-web">www.fennmarsh-example.com</div>
  </footer>
</div>
</body>
</html>
```